Book Cover design for book about character and ethics

This is an exciting book about what it means to live an authentic life. It revolves around finding a sense of contentment, solid friendships and being a good person. The idea is to move away from chasing excessive wealth, good looks and popularity in order to find happiness. Authentic happiness requires a different chase. This book is also about a solid foundation, priorities and work / life balance.

I want a cover that is CREATIVE and POPS. It needs to stand out on the shelf from other books.

Target Market(s)

High school, college and working professionals.

Font styles to use
Serif

Requirements
Must have
• Title: True Otters: Seek A Grounded Path
• Author Name: Dana Vellamore
• Creativity - makes the point without being entirely obvious
• Cover must pop in comparison to other books
• Use bright colors
• Easy to read text
• Cool picture or vector art
Nice to have
• Topics to think about:
• 1. Stand out from the crowd
• 2. The world is lying to you about what makes you happy
• 3. Renewal
• 4. Rebuild
• 5. Chase What Matters
• 6. Pushing against the wind
• I included some pics below as guidance
Should not have
• Cannot be cheesy
• Do not put a rabbit on the cover even though the book is called "True Otters"

```html
<!DOCTYPE html>
<html lang="en">
<head>
<meta charset="utf-8">
<title>True Otters: Seek A Grounded Path — Cover</title>
<link href="https://fonts.googleapis.com/css2?family=Righteous&family=Questrial&display=swap" rel="stylesheet">
<style>
  :root {
    --backdrop: #8d9892;
    --band-crimson: #8f1f2c;
    --band-red: #b8283a;
    --band-orange: #e8892a;
    --band-amber: #eaa23a;
    --strip-light: #e9e5dc;
    --ink-dark: #1c1c1c;
    --type-light: #ffffff;
    --collage-teal: #3fc3c4;
    --collage-ice: #bdf3f8;
    --collage-grey: #7d7d7d;
    --collage-pink: #d98fae;
    --rule-light: #f4efe8;
  }
  html, body {
    margin: 0;
    padding: 0;
    width: 1200px;
    height: 1200px;
    overflow: hidden;
    background: var(--backdrop);
  }
  .cover {
    position: absolute;
    left: 212px;
    top: 50px;
    width: 776px;
    height: 1100px;
    overflow: hidden;
    box-shadow: 0 12px 32px rgba(0,0,0,0.38);
    background: var(--band-red);
  }
  .title-band {
    position: absolute;
    left: 0; top: 0;
    width: 100%;
    height: 128px;
    background: linear-gradient(90deg, var(--band-crimson) 0%, var(--band-red) 35%, var(--band-orange) 75%, var(--band-amber) 100%);
  }
  .book-title {
    position: absolute;
    left: 40px;
    top: 30px;
    margin: 0;
    font-family: "Righteous", sans-serif;
    font-weight: 400;
    font-size: 72px;
    line-height: 1;
    color: var(--type-light);
    letter-spacing: 1px;
  }
  .subtitle-strip {
    position: absolute;
    left: 0; top: 128px;
    width: 100%;
    height: 88px;
    background: linear-gradient(90deg, #ddd8cc, var(--strip-light) 40%, #f3efe6);
  }
  .book-subtitle {
    position: absolute;
    left: 36px;
    top: 16px;
    margin: 0;
    font-family: "Questrial", sans-serif;
    font-weight: 400;
    font-size: 56px;
    line-height: 1;
    color: var(--ink-dark);
  }
  .cover-art {
    position: absolute;
    left: 0; top: 216px;
    width: 100%;
    height: 670px;
    background:
      radial-gradient(ellipse 45% 22% at 65% 12%, rgba(189,243,248,0.95), rgba(189,243,248,0) 100%),
      radial-gradient(ellipse 30% 30% at 8% 20%, rgba(217,143,174,0.75), rgba(217,143,174,0) 100%),
      radial-gradient(ellipse 28% 20% at 72% 62%, rgba(245,245,245,0.9), rgba(245,245,245,0) 100%),
      radial-gradient(ellipse 35% 30% at 12% 85%, rgba(217,143,174,0.8), rgba(217,143,174,0) 100%),
      linear-gradient(180deg, #9fdfe6 0%, #a9a9a9 18%, var(--collage-grey) 35%, #9a9a9a 48%, var(--collage-teal) 62%, #52c9c8 82%, #8fd0d6 100%);
  }
  .rule {
    position: absolute;
    left: 0; top: 886px;
    width: 100%;
    height: 12px;
    background: var(--rule-light);
  }
  .author-band {
    position: absolute;
    left: 0; top: 898px;
    width: 100%;
    height: 202px;
    background: linear-gradient(90deg, #d83a3e 0%, #e2553a 40%, var(--band-orange) 80%, #e79a30 100%);
  }
  .book-author {
    position: absolute;
    left: 72px;
    top: 42px;
    margin: 0;
    font-family: "Questrial", sans-serif;
    font-size: 34px;
    line-height: 1;
    color: var(--type-light);
  }
</style>
</head>
<body>
  <main class="cover">
    <header class="title-band">
      <h1 class="book-title">True Otters</h1>
    </header>
    <div class="subtitle-strip">
      <h2 class="book-subtitle">Seek A Grounded Path</h2>
    </div>
    <div class="cover-art" role="img" aria-label="Collage of torn street posters in pale ice blue, grey, teal and pink, with a dark silhouette of a person swinging on a chain swing across the lower half"></div>
    <div class="rule"></div>
    <footer class="author-band">
      <p class="book-author">Dana Vellamore</p>
    </footer>
  </main>
</body>
</html>
```